Business Card Design Project

I have a two letter domain name vu.com.au (lower case font please). I want a business card, cum logo that is die cut (around the vu segment at least) that fits standard business card size.
vu is all about what 'I am' - a journalist, blogger, analyst, commentator. My mantra is "I think therefore vu'.
The reverse of the card only needs my name Ned Pike, email ned@vu.com.au and mobile +61 400 555 123
Target Market(s)
Mainly people that will use my professional writing services and suppliers that will provide product for review
Industry/Entity Type
Business
Requirements
Must have
- One side is vu.com.au (hint - the .com.au can be vertical or horizontal to fit - the vu should be as large as possible).
The other requires large size font name, email and phone details (so no one needs glasses to read it).
The die cut can be just to highlight the vu segment - need not be around the whole card.
Font used in the past was Belwe (old style - very much like the i used in the information symbol).
Colours - no preference - prefer two colour to process colour but can also be an outline font instead of solid colour.

```html
<!DOCTYPE html>
<html lang="en">
<head>
<meta charset="utf-8">
<title>vu.com.au business card</title>
<link rel="stylesheet" href="https://fonts.googleapis.com/css2?family=Mulish:wght@300;400;700&display=swap">
<style>
  :root {
    --backdrop: #7b7b79;
    --brand-cyan: #00cfff;
    --card-white: #ffffff;
    --ink-dark: #2e3336;
    --text-font: "Mulish", "Century Gothic", sans-serif;
  }
  * { box-sizing: border-box; margin: 0; padding: 0; }
  html, body {
    width: 1200px;
    height: 1000px;
    overflow: hidden;
    background: var(--backdrop);
    font-family: var(--text-font);
  }
  .card-set {
    position: relative;
    width: 1200px;
    height: 1000px;
  }
  .card {
    position: absolute;
    top: 210px;
    width: 340px;
    height: 560px;
    display: flex;
    flex-direction: column;
    align-items: center;
    box-shadow: 0 6px 18px rgba(0, 0, 0, 0.25);
  }
  .card--front {
    left: 220px;
    background: var(--brand-cyan);
  }
  .card--back {
    left: 640px;
    background: var(--card-white);
  }
  .brand-name {
    margin-top: 95px;
    height: 150px;
    font-weight: 700;
    font-size: 150px;
    line-height: 150px;
    letter-spacing: -4px;
  }
  .card--front .brand-name { color: var(--card-white); }
  .card--back .brand-name { color: var(--brand-cyan); font-weight: 400; }
  .domain {
    margin-top: 28px;
    font-weight: 700;
    font-size: 38px;
    color: var(--card-white);
    letter-spacing: 0.5px;
  }
  .tagline {
    margin-top: 2px;
    font-weight: 400;
    font-size: 20px;
    color: var(--ink-dark);
  }
  .contact {
    margin-top: 30px;
    list-style: none;
    text-align: center;
    font-weight: 300;
    font-size: 24px;
    line-height: 30px;
    color: var(--brand-cyan);
  }
</style>
</head>
<body>
  <main class="card-set">
    <section class="card card--front" aria-label="Card front">
      <div class="brand-name">vu</div>
      <p class="domain">vu.com.au</p>
      <p class="tagline">I think therefore vu</p>
    </section>
    <section class="card card--back" aria-label="Card back">
      <div class="brand-name">vu</div>
      <ul class="contact">
        <li class="contact__name">Ned Pike</li>
        <li class="contact__email">ned@vu.com.au</li>
        <li class="contact__phone">+61 400 555 123</li>
      </ul>
    </section>
  </main>
</body>
</html>
```